New IT Consulting Company needs new Branding

I need some business cards and logo created for new IT consulting company called Copperline Partners Pty Ltd.

We deal with enterprise IT solution and IT consulting Firm.
Assisting businesses with Technology Upgrades and System integration

We have no existing color schemes in mind but after something a little recognizable but elegant also.

We are looking for something that conveys a professional look.

Target Market(s)

Targeting small to medium businesses with 0-500 employees

Industry/Entity Type

Information Technology

Contact Information for Business Card

Name, Title , Mobile Contact, Phone Contact , Email and Website URL

Logo Text

CopperPartners Pty Ltd "Shaping Smart Systems with care"

Font styles to use
Serif
Sans Serif

Requirements
Nice to have
• Looking for one or two primary colors and sticking to geometric or symmetrical design for the logo

```html
<!DOCTYPE html>
<html lang="en">
<head>
<meta charset="utf-8">
<title>Copperline Partners – Business Card</title>
<link href="https://fonts.googleapis.com/css2?family=Open+Sans:wght@400;600&display=swap" rel="stylesheet">
<style>
  :root {
    --page-bg: #e6e7ea;
    --card-bg: #f8f8f8;
    --brand-blue: #1a8fd4;
    --text-dark: #2b2b2b;
    --mark-grey: #4a4a4a;
  }
  * { box-sizing: border-box; margin: 0; padding: 0; }
  html, body {
    width: 1200px;
    height: 900px;
    overflow: hidden;
    background: var(--page-bg);
    font-family: "Open Sans", Arial, sans-serif;
  }
  .stage {
    width: 1200px;
    height: 900px;
    display: flex;
    align-items: center;
    justify-content: center;
  }
  .business-card {
    position: relative;
    width: 650px;
    height: 400px;
    background: var(--card-bg);
    border-radius: 16px;
    box-shadow: 0 10px 30px rgba(0,0,0,0.12);
    transform: scale(1.3);
  }
  .brand-mark {
    position: absolute;
    left: 29px;
    top: 40px;
    width: 116px;
    height: 116px;
    border-radius: 50%;
    background: var(--brand-blue);
  }
  .brand-name {
    position: absolute;
    left: 173px;
    top: 58px;
    color: var(--brand-blue);
    font-weight: 600;
    font-size: 30px;
    line-height: 40px;
    letter-spacing: 0.5px;
    text-transform: uppercase;
  }
  .person-name {
    position: absolute;
    left: 175px;
    top: 174px;
    color: var(--brand-blue);
    font-weight: 600;
    font-size: 24px;
    line-height: 32px;
  }
  .person-title,
  .address,
  .contact-list {
    position: absolute;
    left: 175px;
    color: var(--text-dark);
    font-size: 16px;
    line-height: 23px;
  }
  .person-title { top: 205px; }
  .address { top: 243px; }
  .contact-list {
    top: 306px;
    list-style: none;
  }
  .contact-item {
    display: flex;
    align-items: center;
    height: 23.5px;
  }
  .contact-icon {
    width: 13px;
    height: 13px;
    margin-right: 12px;
    fill: var(--brand-blue);
    flex: none;
  }
</style>
</head>
<body>
<main class="stage">
  <article class="business-card">
    <div class="brand-mark"></div>
    <div class="brand-name">Copperline Partners<br>Pty Ltd</div>

    <h1 class="person-name">Daniel Rowe</h1>
    <p class="person-title">Managing Director</p>

    <p class="address">12345, Address Goes Here<br>Country Name, 123456.</p>

    <ul class="contact-list">
      <li class="contact-item">
        <svg class="contact-icon" viewBox="0 0 24 24" aria-hidden="true"><path d="M6.6 10.8c1.4 2.8 3.8 5.1 6.6 6.6l2.2-2.2c.3-.3.7-.4 1-.2 1.1.4 2.3.6 3.6.6.6 0 1 .4 1 1V20c0 .6-.4 1-1 1C10.6 21 3 13.4 3 4c0-.6.4-1 1-1h3.5c.6 0 1 .4 1 1 0 1.3.2 2.5.6 3.6.1.3 0 .7-.2 1z"/></svg>
        044-987 210 436
      </li>
      <li class="contact-item">
        <svg class="contact-icon" viewBox="0 0 24 24" aria-hidden="true"><path d="M2 5h20v14H2z M3 6l9 7 9-7" fill="none" stroke="var(--brand-blue)" stroke-width="0"/><path d="M2 5h20v2l-10 7L2 7z"/><path d="M2 9l10 7 10-7v10H2z"/></svg>
        hello@copperline.net
      </li>
      <li class="contact-item">
        <svg class="contact-icon" viewBox="0 0 24 24" aria-hidden="true"><path d="M10 14a4 4 0 0 0 5.7 0l3.5-3.5a4 4 0 0 0-5.7-5.7l-1.2 1.2M14 10a4 4 0 0 0-5.7 0l-3.5 3.5a4 4 0 0 0 5.7 5.7l1.2-1.2" fill="none" stroke="var(--brand-blue)" stroke-width="2.6" stroke-linecap="round"/></svg>
        www.copperline.net
      </li>
    </ul>
  </article>
</main>
</body>
</html>
```